General Dental Office Business Card

I run a private general dental office in southern California, and would like a refresh/redesign of my business card. I focus on quality care rather than volume. The email address on the uploaded current card should be updated to: info@marbleshoredental.example. The current card's logo is a deboss, but I am open to other ideas. The logo can be refreshed, but it is something that's been with me since the beginning of the office, so I wouldn't want a drastic redesign.
Target Market(s)
Adults 18-99, whoever needs dental services
Industry/Entity Type
Healthcare/Dental
Contact Information for Business Card
Name, Address, Phone, email
Colors
Designer to choose colors to be used in the design.
Requirements
Must have
- Logo (Same as original one in the uploaded file), space on back for appointment time/date

```html
<!DOCTYPE html>
<html lang="en">
<head>
<meta charset="utf-8">
<title>Marble Shore Dental – Business Card</title>
<link href="https://fonts.googleapis.com/css2?family=Lato:wght@300;400;700&display=swap" rel="stylesheet">
<style>
  :root {
    --backdrop: #e6f4fb;
    --card-front: #8dd2ee;
    --pattern: #93d5ef;
    --panel-light: #cdebf8;
    --band-soft: #a9def3;
    --accent: #7ccfee;
    --accent-soft: rgba(255,255,255,0.35);
    --white: #ffffff;
  }
  * { box-sizing: border-box; margin: 0; padding: 0; }
  html, body {
    width: 1200px; height: 1200px; overflow: hidden;
    background: var(--backdrop);
    font-family: "Lato", Arial, sans-serif;
  }
  .card {
    position: absolute; left: 269px; width: 662px; height: 378px; overflow: hidden;
  }
  .card--front { top: 198px; background: var(--card-front); }
  .card--back { top: 630px; background: var(--white); }

  /* front */
  .pattern-field { position: absolute; left: 0; top: 0; width: 552px; height: 378px; background: var(--pattern); }
  .appt-field {
    position: absolute; left: 0; background: var(--panel-light);
    border-radius: 0 24px 24px 0;
  }
  .appt-field--date { top: 24px; width: 216px; height: 48px; }
  .appt-field--time { top: 83px; width: 184px; height: 49px; }
  .appt-field__rule { position: absolute; left: 0; right: 12px; top: 27px; height: 2px; background: var(--accent); }
  .appt-field__label {
    position: absolute; left: 22px; top: 31px;
    font-size: 12px; line-height: 14px; font-weight: 700; color: var(--accent);
  }
  .emblem-ring {
    position: absolute; left: 187px; top: 36px; width: 288px; height: 288px;
    border: 10px solid var(--accent-soft); border-radius: 50%;
  }
  .side-panel { position: absolute; right: 0; top: 0; width: 110px; height: 378px; background: var(--panel-light); }
  .side-panel__band {
    position: absolute; left: 0; top: 0; width: 38px; height: 378px;
    background: linear-gradient(90deg, var(--card-front), var(--band-soft));
  }
  .side-panel__name {
    position: absolute; left: 73px; top: 189px;
    transform: translate(-50%, -50%) rotate(-90deg);
    white-space: nowrap; font-size: 31px; font-weight: 400; color: var(--accent);
  }

  /* back */
  .brand-name {
    position: absolute; left: 37px; top: 185px;
    transform: translate(-50%, -50%) rotate(90deg);
    white-space: nowrap; font-size: 28px; font-weight: 400; color: var(--accent);
  }
  .brand-ring {
    position: absolute; left: 65px; top: 90px; width: 168px; height: 168px;
    border: 7px solid var(--accent); border-radius: 50%;
  }
  .dentist { position: absolute; right: 66px; text-align: right; color: var(--accent); white-space: nowrap; }
  .dentist__name { top: 68px; font-size: 26px; font-weight: 700; }
  .dentist__role { top: 102px; font-size: 19px; font-weight: 400; }
  .dentist__rule { position: absolute; left: 305px; top: 130px; width: 333px; height: 2px; background: var(--accent); }
  .contact { position: absolute; right: 66px; text-align: right; color: var(--accent); font-size: 18px; font-weight: 400; line-height: 25px; white-space: nowrap; }
  .contact--address { top: 176px; }
  .contact--phone { top: 238px; }
  .contact--email { top: 279px; }
  .contact--web { top: 321px; }
  .icon-tab {
    position: absolute; left: 605px; width: 57px; background: var(--accent);
    border-radius: 16px 0 0 16px;
  }
  .icon-tab svg { position: absolute; left: 0; top: 50%; transform: translateY(-50%); }
</style>
</head>
<body>

<section class="card card--front" aria-label="Card front – appointment side">
  <div class="pattern-field" role="img" aria-label="Repeating tonal pattern of the practice emblem"></div>
  <div class="appt-field appt-field--date">
    <div class="appt-field__rule"></div>
    <span class="appt-field__label">Appointment Date</span>
  </div>
  <div class="appt-field appt-field--time">
    <div class="appt-field__rule"></div>
    <span class="appt-field__label">Time</span>
  </div>
  <div class="emblem-ring"></div>
  <div class="side-panel">
    <div class="side-panel__band" role="img" aria-label="Decorative wave edge along the name band"></div>
    <span class="side-panel__name">Marble Shore Dental</span>
  </div>
</section>

<section class="card card--back" aria-label="Card back – contact side">
  <span class="brand-name">Marble Shore Dental</span>
  <div class="brand-ring"></div>

  <div class="dentist dentist__name">Daniel R. Cole DDS</div>
  <div class="dentist dentist__role">General Dentistry</div>
  <div class="dentist__rule"></div>

  <div class="contact contact--address">1280 Harbor Crest Drive<br>Seaview, CA 90000</div>
  <div class="contact contact--phone">555-014-2828</div>
  <div class="contact contact--email">info@marbleshoredental.example</div>
  <div class="contact contact--web">www.marbleshoredental.example</div>

  <div class="icon-tab" style="top:190px;height:32px;">
    <svg width="32" height="32" viewBox="0 0 32 32" fill="none" stroke="#fff" stroke-width="1.6">
      <circle cx="16" cy="16" r="13"/>
      <path d="M16 24 C 12 19, 11 16, 11 13.5 A5 5 0 0 1 21 13.5 C 21 16, 20 19, 16 24 Z"/>
      <circle cx="16" cy="13.5" r="1.8"/>
    </svg>
  </div>
  <div class="icon-tab" style="top:233px;height:32px;">
    <svg width="32" height="32" viewBox="0 0 32 32" fill="none" stroke="#fff" stroke-width="1.6">
      <circle cx="16" cy="16" r="13"/>
      <path d="M11 9 L13.5 9 L15 12.5 L13 14 C 14 16.5, 15.5 18, 18 19 L19.5 17 L23 18.5 L23 21 C 23 22, 22 23, 21 23 C 15 22.5, 9.5 17, 9 11 C 9 10, 10 9, 11 9 Z"/>
    </svg>
  </div>
  <div class="icon-tab" style="top:275px;height:32px;">
    <svg width="32" height="32" viewBox="0 0 32 32" fill="none" stroke="#fff" stroke-width="1.6">
      <circle cx="16" cy="16" r="13"/>
      <rect x="9" y="11" width="14" height="10"/>
      <path d="M9 11 L16 17 L23 11 M9 21 L14 16 M23 21 L18 16"/>
    </svg>
  </div>
  <div class="icon-tab" style="top:318px;height:33px;">
    <svg width="32" height="32" viewBox="0 0 32 32" fill="none" stroke="#fff" stroke-width="1.6">
      <circle cx="16" cy="16" r="13"/>
      <circle cx="16" cy="16" r="8"/>
      <ellipse cx="16" cy="16" rx="3.5" ry="8"/>
      <path d="M8 16 H24 M9.5 12 H22.5 M9.5 20 H22.5"/>
    </svg>
  </div>
</section>

</body>
</html>
```